Brackwell Downs Lamb Sticker Design

We need to create a design for sticky labels that will be placed meat packaging of individual cuts of meat for Brackwell Downs Lamb.

These sticke...

Target Market(s)

People who purchase Gourmet Meat Products. Higher income, Age 35-65

Industry/Entity Type

Farming

Requirements
Must have
• The Brackwell Downs Lamb Logo (attached)
• Quality Grass Fed Lamb
• Need to create a look of premium quality product.
• Space to write Net Weight
• Space to write $

```html
<!DOCTYPE html>
<html lang="en">
<head>
<meta charset="utf-8">
<title>Brackwell Downs Lamb – Meat Labels</title>
<link rel="stylesheet" href="https://fonts.googleapis.com/css2?family=Oswald:wght@600&family=Lobster&family=Permanent+Marker&display=swap">
<style>
  :root {
    --canvas: #f4f3f1;
    --white: #ffffff;
    --gold: #e8b100;
    --gold-light: #f7d24a;
    --gold-deep: #c98f00;
    --red: #c3141d;
    --ink: #1a1a1a;
    --navy: #20252d;
    --tan: #a8927a;
  }
  html, body {
    margin: 0;
    padding: 0;
    width: 1200px;
    height: 675px;
    overflow: hidden;
    background: var(--canvas);
  }
  .canvas {
    position: relative;
    width: 1200px;
    height: 675px;
  }
  .label {
    position: absolute;
    top: 124px;
    width: 166px;
    height: 348px;
    filter: drop-shadow(0 2px 3px rgba(0,0,0,0.18));
  }
  .label--gold { left: 432px; }
  .label--dark { left: 618px; }
  .brand-name {
    font-family: "Oswald", sans-serif;
    font-weight: 600;
    font-size: 17px;
    letter-spacing: 1.5px;
    fill: var(--ink);
  }
  .field-label {
    font-family: "Lobster", cursive;
    font-size: 12px;
  }
  .price {
    font-family: "Permanent Marker", cursive;
    font-size: 21px;
    fill: var(--ink);
  }
  .currency {
    font-family: "Oswald", sans-serif;
    font-weight: 600;
    font-size: 19px;
    fill: var(--white);
  }
  .tagline {
    font-family: "Lobster", cursive;
    font-size: 11px;
  }
  .stars {
    font-family: sans-serif;
    font-size: 12px;
    letter-spacing: 3px;
  }
</style>
</head>
<body>
<main class="canvas">

  <svg class="label label--gold" viewBox="0 0 166 348" aria-label="Brackwell Downs Lamb gold label">
    <defs>
      <linearGradient id="goldFill" x1="0" y1="0" x2="1" y2="1">
        <stop offset="0" stop-color="var(--gold-light)"/>
        <stop offset="0.5" stop-color="var(--gold)"/>
        <stop offset="1" stop-color="var(--gold-deep)"/>
      </linearGradient>
    </defs>
    <polygon points="11,83 155,83 155,348 83,300 11,348" fill="var(--white)"/>
    <circle cx="83" cy="83" r="83" fill="var(--white)"/>
    <polygon points="15,83 151,83 151,340 83,293 15,340" fill="url(#goldFill)"/>
    <circle cx="83" cy="83" r="79" fill="url(#goldFill)"/>
    <polygon points="23,83 143,83 143,322 83,278 23,322" fill="var(--white)"/>
    <polyline points="23,322 83,278 143,322" fill="none" stroke="var(--red)" stroke-width="6"/>
    <circle cx="83" cy="83" r="72" fill="var(--white)"/>
    <circle cx="83" cy="83" r="68" fill="none" stroke="var(--ink)" stroke-width="1.5"/>
    <text class="brand-name" x="83" y="70" text-anchor="middle">BRACKWELL</text>
    <text class="brand-name" x="83" y="92" text-anchor="middle">DOWNS</text>
    <text class="brand-name" x="83" y="114" text-anchor="middle">LAMB</text>

    <text class="field-label" x="34" y="178" fill="var(--red)">Net Weight:</text>
    <line x1="34" y1="194" x2="134" y2="194" stroke="var(--red)" stroke-width="1.5"/>
    <rect x="34" y="202" width="100" height="32" rx="4" fill="var(--white)" stroke="var(--red)" stroke-width="1.5"/>
    <rect x="34" y="202" width="22" height="32" rx="3" fill="var(--red)"/>
    <text class="currency" x="45" y="226" text-anchor="middle">$</text>
    <text class="price" x="95" y="227" text-anchor="middle">39.99</text>
    <text class="tagline" x="84" y="248" text-anchor="middle" fill="var(--red)">Quality Grass Fed Lamb</text>
    <text class="stars" x="85" y="262" text-anchor="middle" fill="var(--red)">★★★★★</text>
  </svg>

  <svg class="label label--dark" viewBox="0 0 166 348" aria-label="Brackwell Downs Lamb dark label">
    <polygon points="11,83 155,83 155,348 83,300 11,348" fill="var(--white)"/>
    <circle cx="83" cy="83" r="83" fill="var(--white)"/>
    <polygon points="15,83 151,83 151,340 83,293 15,340" fill="var(--tan)"/>
    <circle cx="83" cy="83" r="79" fill="var(--tan)"/>
    <polygon points="23,83 143,83 143,322 83,278 23,322" fill="var(--navy)"/>
    <polyline points="23,322 83,278 143,322" fill="none" stroke="var(--white)" stroke-width="5"/>
    <circle cx="83" cy="83" r="72" fill="var(--white)"/>
    <circle cx="83" cy="83" r="68" fill="none" stroke="var(--ink)" stroke-width="1.5"/>
    <text class="brand-name" x="83" y="70" text-anchor="middle">BRACKWELL</text>
    <text class="brand-name" x="83" y="92" text-anchor="middle">DOWNS</text>
    <text class="brand-name" x="83" y="114" text-anchor="middle">LAMB</text>

    <rect x="34" y="168" width="100" height="28" rx="4" fill="var(--white)" stroke="var(--tan)" stroke-width="1.5"/>
    <text class="field-label" x="38" y="181" fill="var(--tan)">Net Weight:</text>
    <rect x="34" y="202" width="100" height="32" rx="4" fill="var(--white)" stroke="var(--tan)" stroke-width="1.5"/>
    <rect x="34" y="202" width="22" height="32" rx="3" fill="var(--tan)"/>
    <text class="currency" x="45" y="226" text-anchor="middle">$</text>
    <text class="price" x="95" y="227" text-anchor="middle">39.99</text>
    <text class="tagline" x="84" y="248" text-anchor="middle" fill="var(--tan)">Quality Grass Fed Lamb</text>
    <text class="stars" x="85" y="262" text-anchor="middle" fill="var(--tan)">★★★★★</text>
  </svg>

</main>
</body>
</html>
```